New business card design to go with our new logo

just want an eye-catching business card to go with our new logo. We are open to double sided or single sided. Just want it to have the following info on it. Whatever layout you think looks best.

First and Last Name
Title
Phone 801-555-0187
Address 312 W. Larkmoor Avenue Orem UT 84057
Email thecrew@meadowstailandkennel.example

Industry/Entity Type

Business

```html
<!DOCTYPE html>
<html lang="en">
<head>
<meta charset="utf-8">
<title>Meadow's Tail &amp; Kennel — Business Card</title>
<link rel="stylesheet" href="https://fonts.googleapis.com/css2?family=Crimson+Text:wght@400;700&display=swap">
<style>
  :root {
    --backdrop: #2b2a29;
    --card-orange: #f08a4b;
    --card-black: #141414;
    --accent-blue: #2b9fde;
    --text-light: #f4f4f4;
  }
  * { margin: 0; padding: 0; box-sizing: border-box; }
  html, body {
    width: 1200px;
    height: 716px;
    overflow: hidden;
    background: var(--backdrop);
  }
  .stage {
    position: relative;
    width: 1200px;
    height: 716px;
  }
  .business-card {
    position: absolute;
    left: 110px;
    top: 78px;
    width: 980px;
    height: 560px;
    overflow: hidden;
    box-shadow: 0 18px 40px rgba(0,0,0,0.45);
  }
  .card-art {
    position: absolute;
    inset: 0;
    width: 980px;
    height: 560px;
    display: block;
  }
  .brand-name {
    position: absolute;
    left: 130px;
    top: 250px;
    width: 300px;
    text-align: center;
    color: var(--text-light);
    font-family: "Crimson Text", serif;
    font-weight: 700;
    font-size: 30px;
    line-height: 1.15;
    letter-spacing: 1px;
  }
  .contact {
    position: absolute;
    left: 520px;
    top: 228px;
    color: var(--text-light);
    font-family: "Crimson Text", serif;
  }
  .person-name,
  .person-title {
    font-size: 27px;
    font-weight: 700;
    letter-spacing: 1.5px;
    line-height: 1.1;
  }
  .person-title {
    margin-bottom: 20px;
  }
  .contact-line {
    font-size: 16px;
    line-height: 1.4;
  }
  .contact-address {
    margin-top: 12px;
  }
</style>
</head>
<body>
<main class="stage">
  <section class="business-card" aria-label="Business card">
    <svg class="card-art" viewBox="0 0 980 560" aria-hidden="true">
      <rect width="980" height="560" fill="var(--card-orange)"/>
      <ellipse cx="640" cy="200" rx="576" ry="346" fill="var(--accent-blue)"/>
      <ellipse cx="640" cy="200" rx="570" ry="340" fill="var(--card-black)"/>
      <line x1="440" y1="80" x2="980" y2="80" stroke="var(--accent-blue)" stroke-width="3"/>
    </svg>

    <p class="brand-name">Meadow's Tail<br>&amp; Kennel</p>

    <div class="contact">
      <p class="person-name">First &amp; Last Name</p>
      <p class="person-title">Title</p>
      <p class="contact-line">801-555-0187</p>
      <p class="contact-line">thecrew@meadowstailandkennel.example</p>
      <p class="contact-line contact-address">312 W. Larkmoor Avenue Orem</p>
      <p class="contact-line">UT 84057</p>
    </div>
  </section>
</main>
</body>
</html>
```